Oil and Gas Letterhead Design Tweak

Simple letterhead information and design tweak.

Please note, we don't want to change the design or logo of the letterhead only the small changes mentioned below.

We need to change the company name up top to "Northvale Petrotek FZCO"

Also, we need to include in the footer the following information. I have attached an image of roughly how we would like to have it displayed in the footer.

Footer Details:

Northvale Petrotek FZCO,
Unit No. 2378, FZCO Trade Hub, level No. 1, K&P 7, Dubai, United Arab Emirates
Northvale Petrotek FZCO is registered as a free zone company under the rules & regulations of FZCO

Target Market(s)

O&G Market

Industry/Entity Type

Oil And Gas

Font styles to use
Sans Serif

Colors

Designer to choose colors to be used in the design.

Requirements
Must have
• Change the company name to Northvale Petrotek FZCO
• Include the footer on the bottom of the first and continuation page
Should not have
• Should not change the design or logo of the letterhead, only the specified changes mentioned above

```html
<!DOCTYPE html>
<html lang="en">
<head>
<meta charset="utf-8">
<title>Northvale Petrotek FZCO – Letterhead</title>
<link href="https://fonts.googleapis.com/css2?family=Abel&display=swap" rel="stylesheet">
<style>
  :root {
    --brand-blue: #1b2a8f;
    --brand-red: #f00000;
    --paper: #fdfdfd;
  }
  html, body {
    margin: 0;
    padding: 0;
    overflow: hidden;
    background: var(--paper);
  }
  .letterhead {
    position: relative;
    width: 848px;
    height: 1200px;
    overflow: hidden;
    background: var(--paper);
    font-family: "Abel", "Arial Narrow", sans-serif;
    color: var(--brand-blue);
  }
  .accent-bars {
    position: absolute;
    left: 0;
    top: 0;
  }
  .company-name {
    position: absolute;
    left: 268px;
    top: 44px;
    margin: 0;
    font-size: 33px;
    font-weight: 400;
    line-height: 1;
    letter-spacing: 0.3px;
    text-transform: uppercase;
    color: var(--brand-blue);
  }
  .footer-details {
    position: absolute;
    left: 30px;
    top: 1146px;
    margin: 0;
    font-size: 11.6px;
    line-height: 13.5px;
    text-transform: uppercase;
    color: var(--brand-blue);
  }
  .footer-details p {
    margin: 0;
  }
</style>
</head>
<body>
<main class="letterhead">
  <svg class="accent-bars" width="848" height="1200" viewBox="0 0 848 1200" aria-hidden="true">
    <polygon class="bar-blue" points="0,0 195,0 188,15.7 0,15.7" fill="var(--brand-blue)"/>
    <polygon class="bar-red" points="263,0 848,0 848,15.7 270,15.7" fill="var(--brand-red)"/>
    <polygon class="tab-blue" points="623,1184.5 658,1184.5 651,1200 615,1200" fill="var(--brand-blue)"/>
    <polygon class="tab-red" points="668,1184.5 696,1184.5 703,1200 660,1200" fill="var(--brand-red)"/>
  </svg>

  <h1 class="company-name">Northvale Petrotek FZCO</h1>

  <footer class="footer-details">
    <p>Northvale Petrotek FZCO,</p>
    <p>Unit No. 2378, FZCO Trade Hub, level No. 1, K&amp;P 7, Dubai, United Arab Emirates</p>
    <p>Northvale Petrotek FZCO is registered as a free zone company under the rules &amp; regulations of FZCO</p>
  </footer>
</main>
</body>
</html>
```